Protrait photographers business card

Need a new catchy, chic business card to promote my new portrait photograghy business. Love taking the natural, location portraits of families, children, teens. It should look classy, but also warm & friendly. I want it to show that Famliy, friends, couples & childten are what I love photographing, so if it can have that sort of feel to it & also looking energetic.

Target Market(s)

Families, couples, babies, people on holidays wanting some locational professional photos

Industry/Entity Type

Portrait Photography

Contact Information for Business Card

Lumivale photography, By Tavi, Norah Balfrey,Ph: 0487356024, Kestrel cove, Qld

Font styles to use
Decorative
Script

Requirements
Must have
• Company name & photographers name
Nice to have
• a coloured card
Should not have
• not be on a white card

```html
<!DOCTYPE html>
<html lang="en">
<head>
<meta charset="utf-8">
<title>Lumivale photography – business card</title>
<link href="https://fonts.googleapis.com/css2?family=Parisienne&family=Dancing+Script:wght@400&display=swap" rel="stylesheet">
<style>
  :root {
    --backdrop: #e9e6e8;
    --card-black: #0b0b0c;
    --card-glow: #4a4a4d;
    --berry: #d8237a;
    --violet: #8a46a8;
    --lilac: #9a63c0;
    --ink-white: #f2eef2;
    --frame: #ffffff;
  }
  * { margin: 0; padding: 0; box-sizing: border-box; }
  html, body {
    width: 1200px; height: 828px; overflow: hidden;
    background: var(--backdrop);
  }
  .card {
    position: absolute; left: 100px; top: 128px;
    width: 1000px; height: 572px; overflow: hidden;
    background: radial-gradient(ellipse 55% 70% at 42% 45%, var(--card-glow) 0%, #1c1c1e 55%, var(--card-black) 100%);
    box-shadow: 0 10px 30px rgba(0,0,0,.25);
  }
  .band { position: absolute; display: block; }
  .band--top { left: 0; top: 0; width: 1000px; height: 40px; }
  .band--bottom { left: 0; bottom: 0; width: 1000px; height: 50px; }

  .photo {
    position: absolute; border: 6px solid var(--frame);
    box-shadow: 0 4px 10px rgba(0,0,0,.6);
  }
  .photo--couple-outdoor { left: 250px; top: 48px; width: 172px; height: 126px; transform: rotate(3deg);
    background: linear-gradient(135deg, #dfe6d6, #b9a99a 55%, #5d6a7a); }
  .photo--couple-close { left: 404px; top: 108px; width: 180px; height: 136px; transform: rotate(6deg);
    background: linear-gradient(120deg, #e6d2c4, #c89a86 50%, #3a2a2c); }
  .photo--portrait { left: 226px; top: 166px; width: 192px; height: 146px; transform: rotate(-5deg);
    background: linear-gradient(140deg, #d9cfc4, #8a6a58 50%, #2a1e1c); }

  .photographer {
    position: absolute; left: 56px; top: 350px;
    font-family: "Parisienne", cursive; font-size: 58px; color: var(--lilac);
  }
  .email {
    position: absolute; left: 60px; top: 425px;
    font-family: "Dancing Script", cursive; font-size: 23px; color: var(--ink-white);
  }
  .brand {
    position: absolute; left: 655px; top: 118px; color: var(--berry);
    font-family: "Parisienne", cursive; font-weight: 400;
  }
  .brand__name { display: block; font-size: 74px; line-height: 1; }
  .brand__tag { display: block; font-size: 42px; margin: 8px 0 0 70px; }
  .contact {
    position: absolute; left: 630px; font-family: "Dancing Script", cursive;
    font-size: 30px; color: var(--lilac);
  }
  .contact--place { top: 370px; }
  .contact--phone { top: 440px; }
</style>
</head>
<body>
  <main class="card">
    <svg class="band band--top" viewBox="0 0 1000 40" aria-hidden="true">
      <polygon points="250,0 720,0 640,40 250,40" fill="var(--violet)"/>
    </svg>

    <div class="photo photo--couple-outdoor" role="img" aria-label="Photo of a couple outdoors"></div>
    <div class="photo photo--couple-close" role="img" aria-label="Close-up photo of a couple"></div>
    <div class="photo photo--portrait" role="img" aria-label="Portrait photo of a woman"></div>

    <p class="photographer">Norah Balfrey</p>
    <p class="email">lumivalephotography@mailbox.com</p>

    <h1 class="brand">
      <span class="brand__name">Lumivale</span>
      <span class="brand__tag">photography</span>
    </h1>

    <p class="contact contact--place">Kestrel cove, Qld</p>
    <p class="contact contact--phone">Ph. 048 735 6024</p>

    <svg class="band band--bottom" viewBox="0 0 1000 50" aria-hidden="true">
      <polygon points="330,0 730,0 730,50 260,50" fill="var(--berry)"/>
    </svg>
  </main>
</body>
</html>
```